Long Established Local Fencing (not swords) Business needs fresh Business Cards

We need fresh double sided business cards for our Fencing Construction business, we are looking for something with our new logo design added, and maybe a photo background ?
We recently had cards made from Cardlyne and we were horrified with what we got back, the quality was terrible, so am looking for high quality format for good printing company to make.
We install Steelmora, Timber paling, Aluminium Slat Screening, Picket (timber and aluminium) and most other fencing installations.
Our website is brankelrails.com.au should you like to learn a bit more.
We do have logo in other formats if required.
We have been in business for over 35 years and we have used this as a "motto" it is on our signage

Industry/Entity Type

Construction

Contact Information for Business Card

Open to ideas, we need 3 x different cards, one generic with no name and 2 x others each with 1 of our bosses name on each, I will put into upload files.

Colors
ec1f27
000000
606060
f5f5f5

Requirements
Must have
• Company Name and Logo
• Address
• Contact details, phone, website, email etc
• Small space to write notes when leaving card at residence
Nice to have
• Our motto "Servicing the Peninsula for over 35 years"

```html
<!DOCTYPE html>
<html lang="en">
<head>
<meta charset="utf-8">
<title>Brankel Rails – Business Cards</title>
<link rel="stylesheet" href="https://fonts.googleapis.com/css2?family=Open+Sans:wght@400;600;700;800&display=swap">
<style>
  :root {
    --brand-red: #ec1f27;
    --brand-black: #000000;
    --brand-grey: #606060;
    --paper: #f5f5f5;
    --card: #ffffff;
    --backdrop: #2b2b2b;
    --rule: #b8b8b8;
  }
  * { box-sizing: border-box; margin: 0; padding: 0; }
  html, body { width: 1200px; height: 900px; overflow: hidden; }
  body {
    background: var(--backdrop);
    font-family: "Open Sans", Arial, sans-serif;
    display: flex;
    flex-direction: column;
    align-items: center;
    justify-content: center;
    gap: 44px;
  }
  .card {
    position: relative;
    width: 660px;
    height: 377px;
    background: var(--card);
    box-shadow: 0 10px 30px rgba(0,0,0,.45);
    overflow: hidden;
  }

  /* Back side: notes */
  .notes-mark {
    position: absolute;
    left: 50%;
    top: 46px;
    width: 220px;
    height: 220px;
    margin-left: -110px;
    border-radius: 50%;
    background: var(--brand-grey);
    opacity: .07;
  }
  .notes-lines {
    position: absolute;
    left: 60px;
    right: 60px;
    top: 42px;
    list-style: none;
  }
  .notes-lines li {
    height: 38px;
    border-bottom: 1px dotted var(--rule);
  }
  .motto {
    position: absolute;
    left: 0; right: 0;
    bottom: 34px;
    text-align: center;
    font-size: 13px;
    color: var(--brand-grey);
  }

  /* Front side */
  .front-band { position: absolute; left: 0; top: 0; }
  .brand {
    position: absolute;
    left: 40px;
    top: 196px;
    width: 250px;
    display: flex;
    align-items: center;
    gap: 12px;
  }
  .brand-dot {
    width: 26px; height: 26px;
    border-radius: 50%;
    background: var(--brand-red);
    flex: none;
  }
  .brand-name {
    font-weight: 800;
    font-size: 27px;
    line-height: 1.05;
    letter-spacing: .5px;
    color: var(--brand-black);
    text-transform: uppercase;
  }
  .divider {
    position: absolute;
    left: 320px;
    top: 100px;
    width: 1px;
    height: 190px;
    background: #d0d0d0;
  }
  .contact {
    position: absolute;
    left: 345px;
    top: 98px;
    color: var(--brand-grey);
    font-size: 14px;
    line-height: 20px;
  }
  .contact-name {
    color: var(--brand-red);
    font-weight: 700;
    font-size: 17px;
    margin-bottom: 6px;
    text-transform: uppercase;
  }
  .contact-row { display: flex; align-items: center; gap: 8px; }
  .contact-row svg { width: 13px; height: 13px; flex: none; }
</style>
</head>
<body>

  <section class="card card-back" aria-label="Card back with notes space">
    <div class="notes-mark"></div>
    <ol class="notes-lines">
      <li></li><li></li><li></li><li></li><li></li><li></li><li></li>
    </ol>
    <p class="motto">Servicing the Peninsula for over 35 years</p>
  </section>

  <section class="card card-front" aria-label="Card front with contact details">
    <svg class="front-band" width="660" height="80" viewBox="0 0 660 80">
      <polygon points="0,0 660,0 660,4 0,60" fill="#d9d9d9"/>
      <polygon points="0,0 660,0 660,2 0,44" fill="var(--brand-red)"/>
    </svg>

    <div class="brand">
      <span class="brand-dot"></span>
      <span class="brand-name">Brankel<br>Rails</span>
    </div>

    <div class="divider"></div>

    <div class="contact">
      <p class="contact-name">Dorian Vell</p>
      <p>27 Harlow St Brankel</p>
      <p>License No: 51624k</p>
      <p>ABN 42 815 07 936</p>
      <p class="contact-row">
        <svg viewBox="0 0 16 16"><path fill="var(--brand-red)" d="M2 5c0-2 2-3 6-3s6 1 6 3l-3 1-1-2H6L5 6 2 5zm2 2h8l2 6H2l2-6zm4 1.5a2 2 0 100 4 2 2 0 000-4z"/></svg>
        (02)40185527
      </p>
      <p class="contact-row">
        <svg viewBox="0 0 16 16"><rect x="4" y="1" width="8" height="14" rx="1.5" fill="var(--brand-red)"/><rect x="5.5" y="3" width="5" height="8" fill="#fff"/></svg>
        0428 604 371
      </p>
      <p class="contact-row">
        <svg viewBox="0 0 16 16"><rect x="1" y="3" width="14" height="10" rx="1" fill="var(--brand-red)"/><path d="M1.5 3.5 8 9l6.5-5.5" stroke="#fff" stroke-width="1.3" fill="none"/></svg>
        office@brankelrails.com.au
      </p>
      <p class="contact-row">
        <svg viewBox="0 0 16 16"><circle cx="8" cy="8" r="7" fill="var(--brand-red)"/><path d="M1 8h14M8 1c-3 3-3 11 0 14M8 1c3 3 3 11 0 14" stroke="#fff" stroke-width="1" fill="none"/></svg>
        www.brankelrails.com.au
      </p>
    </div>
  </section>

</body>
</html>
```